Business Card for By Marcus Hale

Looking to have a business card designed for my lifestyle and fitness company. My company offers personal training, online programming and nutrition advice based out of London, United Kingdom.

I'd like to see modern, sleek designs, focusing on black, matte black or matte grey. Design doesn't need to be overly descriptive as this will also be used as a personal business card. I've included my logo.

Please note that my company is no longer called "Fitness by Marcus Hale" but instead "By Marcus Hale", this is because of my other ventures. Therefore please don't use the "fitness by marcus hale" text.

information about my company can be found at www.bymarcushale.com

Company is also based out of London (United Kingdom) & Sydney (Australia) this could be reflected on the card.

Industry/Entity Type

Business

Contact Information for Business Card

Marcus Hale
+44 7382 615204
marcus@bymarcushale.com
www.bymarcushale.com

Font styles to use
Sans Serif

Requirements
Must have
• All contact details and inclusion of my logo.

```html
<!DOCTYPE html>
<html lang="en">
<head>
<meta charset="utf-8">
<title>By Marcus Hale — Business Card</title>
<link rel="stylesheet" href="https://fonts.googleapis.com/css2?family=Lato:wght@400;700&display=swap">
<style>
  :root {
    --page-bg: #e9e7e4;
    --card-black: #141414;
    --card-edge: #2a2a2a;
    --ink-white: #ffffff;
    --ink-soft: #e6e6e6;
    --rule-grey: #9a9a9a;
    --social-blue: #3b5b94;
    --social-sky: #3fa9e0;
    --social-steel: #4a6f96;
  }
  * { margin: 0; padding: 0; box-sizing: border-box; }
  html, body {
    width: 1200px; height: 900px; overflow: hidden;
    background: var(--page-bg);
    font-family: "Lato", Arial, sans-serif;
  }
  .stage { position: relative; width: 1200px; height: 900px; }
  .card {
    position: absolute;
    width: 580px; height: 330px;
    background: var(--card-black);
    border-radius: 3px;
    box-shadow: 0 0 0 1px var(--card-edge), 0 14px 30px rgba(0,0,0,.25);
    color: var(--ink-white);
  }
  /* Logo side */
  .card--back { left: 110px; top: 130px; }
  .card--back .brand-mark {
    position: absolute; left: 0; right: 0; top: 105px;
    text-align: center;
    font-weight: 700; font-size: 30px; letter-spacing: 3px;
    text-transform: uppercase;
  }
  .card--back .divider {
    position: absolute; left: 110px; right: 110px; top: 222px;
    height: 1px; background: var(--rule-grey);
  }
  .card--back .social-row {
    position: absolute; left: 50%; top: 212px;
    transform: translateX(-50%);
    display: flex; gap: 6px;
    background: var(--card-black); padding: 0 8px;
  }
  .social-row span { width: 20px; height: 20px; display: block; }
  .social-row .s1 { background: var(--social-blue); }
  .social-row .s2 { background: var(--social-sky); }
  .social-row .s3 { background: var(--social-steel); }

  /* Contact side */
  .card--front { left: 510px; top: 440px; }
  .card--front .brand-mark {
    position: absolute; right: 36px; top: 92px;
    font-weight: 700; font-size: 24px; letter-spacing: 2px;
    text-transform: uppercase;
  }
  .card--front .brand-rule {
    position: absolute; right: 36px; top: 130px;
    width: 232px; height: 2px; background: var(--ink-white);
  }
  .contact { position: absolute; left: 40px; bottom: 34px; }
  .contact__name {
    font-weight: 700; font-size: 20px; letter-spacing: 1px;
    text-transform: uppercase; margin-bottom: 12px;
  }
  .contact__line {
    display: flex; align-items: center; gap: 9px;
    font-size: 16px; color: var(--ink-soft); line-height: 25px;
    padding-left: 10px;
  }
  .contact__line svg { width: 14px; height: 14px; fill: var(--ink-soft); flex: none; }
</style>
</head>
<body>
<main class="stage">
  <section class="card card--back">
    <div class="brand-mark">By Marcus Hale</div>
    <div class="divider"></div>
    <div class="social-row"><span class="s1"></span><span class="s2"></span><span class="s3"></span></div>
  </section>

  <section class="card card--front">
    <div class="brand-mark">By Marcus Hale</div>
    <div class="brand-rule"></div>
    <div class="contact">
      <p class="contact__name">Marcus Hale</p>
      <p class="contact__line">
        <svg viewBox="0 0 16 16" aria-hidden="true"><path d="M3 2h3l1.5 3.5-2 1.3a8 8 0 0 0 3.7 3.7l1.3-2L14 10v3a1 1 0 0 1-1 1A11 11 0 0 1 2 3a1 1 0 0 1 1-1z"/></svg>
        +44 7382 615204
      </p>
      <p class="contact__line">
        <svg viewBox="0 0 16 16" aria-hidden="true"><path d="M1 3h14v10H1z M2 4.2v.6l6 4 6-4v-.6z" fill-rule="evenodd"/></svg>
        marcus@bymarcushale.com
      </p>
      <p class="contact__line">
        <svg viewBox="0 0 16 16" aria-hidden="true"><circle cx="8" cy="8" r="7"/><path d="M1 8h14M8 1c3 3 3 11 0 14M8 1c-3 3-3 11 0 14" stroke="#141414" stroke-width="1" fill="none"/></svg>
        www.bymarcushale.com
      </p>
    </div>
  </section>
</main>
</body>
</html>
```